New innovative Legal start-up looking for letterhead and business card template

Using our existing logo, colours and font we need a simple, professional, accessible (easy to read), and consistent letterhead and business card design template. Letterhead will be printed in house so heavy colour is not preferred (though some colour is acceptable). Letter sis is US Letter (21.59 cm x 27.94cm) and business card is standard size (3.5"x 2")Logo Proof sheet is attached. Logo designs can be found here https://www.stashvane.net/sh/qt4rp9zkw2vhn81/KLM7XQ3gTpbRwHsN4e2fzYdVc?dl=0

```html
<!DOCTYPE html>
<html lang="en">
<head>
<meta charset="utf-8">
<title>Brightwell Counsel – Stationery</title>
<link rel="stylesheet" href="https://fonts.googleapis.com/css2?family=Lato:wght@400;700&family=Roboto+Condensed:wght@400;500&display=swap">
<style>
:root{
  --bg:#3a3a3a;
  --paper:#ffffff;
  --ink:#1d1d1d;
  --grey:#8f8f8f;
  --grey-card:#959595;
  --teal:#3aa89d;
  --navy:#2f3553;
  --orange:#f0842c;
}
*{margin:0;padding:0;box-sizing:border-box}
html,body{width:1189px;height:1200px;overflow:hidden;background:var(--bg)}
body{position:relative;font-family:'Roboto Condensed',sans-serif;color:var(--ink)}

.letterhead{position:absolute;left:273px;top:53px;width:648px;height:840px;background:var(--paper)}
.brand{position:absolute;display:flex;align-items:center;gap:8px;font-family:'Lato',sans-serif}
.brand-mark{flex:none;border-radius:50%;border:3px solid var(--grey)}
.brand-name{color:var(--grey);font-weight:400;line-height:1.1;letter-spacing:.5px}
.letterhead .brand{left:401px;top:69px}
.letterhead .brand-mark{width:65px;height:65px}
.letterhead .brand-name{font-size:22px;width:150px}

.recipient{position:absolute;left:52px;top:252px;font-size:11px;line-height:13px}
.recipient-name{font-size:13px;font-weight:500;margin-bottom:6px}

.letter{position:absolute;left:53px;top:339px;width:544px;font-size:11.3px;line-height:19px}
.letter-body p{text-align:justify}
.letter-body p + p{margin-top:19px}
.regards{line-height:14px}
.signature{width:150px;height:44px;margin-top:22px;background:linear-gradient(90deg,#e6e6e6,#f4f4f4);border-radius:4px}
.sender{margin-top:6px;font-size:13px;font-weight:500}

.footer-rule{position:absolute;left:53px;top:776px;width:540px;height:1.5px;background:var(--orange)}
.footer{position:absolute;top:785px;font-family:'Lato',sans-serif;font-size:11px;line-height:14px;color:var(--grey)}
.footer-row{display:flex;align-items:center;gap:3px}
.dot{display:inline-block;flex:none;width:10px;height:10px;border-radius:50%;border:1.5px solid currentColor}
.dot.teal{color:var(--teal)}
.dot.navy{color:var(--navy)}
.dot.orange{color:var(--orange)}
.footer-sep{position:absolute;top:787px;width:1.5px;height:25px;background:var(--orange)}

.card{position:absolute;top:938px;width:319px;height:182px;overflow:hidden}
.card-front{left:273px;background:var(--paper);border-radius:8px 0 0 8px}
.card-back{left:603px;background:var(--grey-card);border-radius:0 8px 8px 0}
.card .brand{gap:6px}
.card .brand-mark{width:48px;height:48px;border-width:2px}
.card .brand-name{font-size:15px;width:100px}
.card-front .brand{left:16px;top:18px}
.card-back .brand{left:155px;top:20px}
.card-back .brand-mark{border-color:#fff}
.card-back .brand-name{color:#fff}
.holder{position:absolute;left:17px;top:82px;font-family:'Lato',sans-serif;color:var(--grey);font-size:11px;line-height:11px}
.holder-role{color:var(--orange);font-size:9px}
.card-address{position:absolute;left:17px;top:108px;font-family:'Lato',sans-serif;font-size:8px;line-height:11px;color:var(--grey)}
.card-contact{position:absolute;left:17px;top:136px;font-family:'Lato',sans-serif;font-size:8px;line-height:11.5px;color:var(--grey)}
.card-contact .dot{width:8px;height:8px;border-width:1.2px}
.card-web{position:absolute;right:18px;bottom:12px;font-family:'Lato',sans-serif;font-size:8px;color:#fff}
.ring{position:absolute;top:0}
</style>
</head>
<body>

<section class="letterhead">
  <div class="brand">
    <span class="brand-mark"></span>
    <span class="brand-name">Brightwell Counsel</span>
  </div>

  <div class="recipient">
    <div class="recipient-name">JANE MARLOW</div>
    <div>Street Name,City Name.</div>
    <div>Zip Coad 0000</div>
  </div>

  <div class="letter">
    <div class="letter-body">
      <p>Lorem Ipsum is simply dummy text of the printing and typesetting industry. Lorem Ipsum has been the industry's standard dummy text ever since the 1500s, when an unknown printer took a galley of type and scrambled it to make a type specimen book. It has survived not only five centuries, but also the leap into electronic typesetting, remaining essentially unchanged. It was popularised in the 1960s with the release of Letraset sheets containing Lorem Ipsum passages, and more recently with desktop publishing software like Aldus PageMaker including versions of Lorem Ipsum.</p>
      <p>It is a long established fact that a reader will be distracted by the readable content of a page when looking at its layout. The point of using Lorem Ipsum is that it has a more-or-less normal distribution of letters, as opposed to using 'Content here, content here', making it look like readable English. Many desktop publishing packages and web page editors now use Lorem Ipsum as their default model text, and a search for 'lorem ipsum' will uncover many web sites still in their infancy. Various versions have evolved over the years, sometimes by accident, sometimes on purpose.</p>
    </div>
    <div class="regards">Regards,</div>
    <div class="signature" role="img" aria-label="Handwritten signature of Tom Reyes"></div>
    <div class="sender">Tom Reyes</div>
  </div>

  <div class="footer-rule"></div>
  <div class="footer" style="left:63px">
    <div class="footer-row"><span class="dot teal"></span>(01) 2345 6789</div>
    <div class="footer-row"><span class="dot teal"></span>(01) 2345 6789</div>
  </div>
  <div class="footer-sep" style="left:190px"></div>
  <div class="footer" style="left:231px">
    <div class="footer-row"><span class="dot navy"></span>info@companymail.com</div>
    <div class="footer-row"><span class="dot navy"></span>www.companyweb.com</div>
  </div>
  <div class="footer-sep" style="left:408px"></div>
  <div class="footer" style="left:452px;top:787px">
    <div>PO BOX 123 your address,</div>
    <div>2nd street london ,USA</div>
  </div>
</section>

<section class="card card-front">
  <div class="brand">
    <span class="brand-mark"></span>
    <span class="brand-name">Brightwell Counsel</span>
  </div>
  <div class="holder">
    <div>ELLIS CRANE</div>
    <div class="holder-role">Manager</div>
  </div>
  <div class="card-address">
    <div>PO BOX 123 your address,</div>
    <div>2nd street london ,USA</div>
  </div>
  <div class="card-contact">
    <div class="footer-row"><span class="dot teal"></span>(01) 2345 6789</div>
    <div class="footer-row"><span class="dot navy"></span>info@companymail.com</div>
    <div class="footer-row"><span class="dot orange"></span>www.companyweb.com</div>
  </div>
  <svg class="ring" style="left:226px" width="93" height="182" viewBox="0 0 93 182">
    <circle cx="93" cy="91" r="88" fill="none" stroke="#a3a3a3" stroke-width="5"/>
  </svg>
</section>

<section class="card card-back">
  <svg class="ring" style="left:0" width="90" height="182" viewBox="0 0 90 182">
    <circle cx="0" cy="91" r="84" fill="none" stroke="#ffffff" stroke-width="5"/>
  </svg>
  <div class="brand">
    <span class="brand-mark"></span>
    <span class="brand-name">Brightwell Counsel</span>
  </div>
  <div class="card-web">www.companyweb.com</div>
</section>

</body>
</html>
```